Personal Brand Business Card

I am looking for a design that I will use as my personal brand that conveys class (think 1920s gentlemen) and is timeless. I will be putting this on a pearl white, letter pressed, cotton business card.  I’m thinking maybe something with my initials on the front they will flip over for the rest of my information.  But don’t let that limit you.
The information I will have on the back of the business card will be my name, email, and phone number.
Some of the attributes that best describe me are: loyal, dependable, creative, risk taker, open minded, competitive, and empathetic.  I can adapt to my environment quickly and can get along with anyone.  I get excited by figuring out the way things work and finding solutions to problems.

Industry/Entity Type
Business

```html
<!DOCTYPE html>
<html lang="en">
<head>
<meta charset="utf-8">
<title>Grant Halloway – Business Card Presentation</title>
<link rel="stylesheet" href="https://fonts.googleapis.com/css2?family=Cormorant+Garamond:wght@500;600&family=Tinos&display=swap">
<style>
  :root {
    --brown: #4e3100;
    --paper: #ffffff;
    --paper-edge: #d6d6d6;
    --board-light: #ffffff;
    --board-dark: #d3d3d3;
    --frame: #9a9a9a;
    --label: #111111;
  }
  * { margin: 0; padding: 0; box-sizing: border-box; }
  html, body { width: 1200px; height: 720px; overflow: hidden; }
  body {
    position: relative;
    background: radial-gradient(ellipse 60% 55% at 50% 45%, var(--board-light) 0%, #f1f1f1 45%, var(--board-dark) 100%);
    font-family: "Cormorant Garamond", Georgia, serif;
  }
  .band { position: absolute; left: 0; width: 1200px; background: var(--brown); }
  .band--top { top: 0; height: 59px; }
  .band--bottom { top: 647px; height: 73px; }

  .card {
    position: absolute;
    top: 177px;
    width: 543px;
    height: 313px;
    border: 2px solid var(--frame);
    background: radial-gradient(ellipse 65% 70% at 50% 50%, var(--paper) 0%, #f6f6f6 50%, var(--paper-edge) 100%);
    overflow: hidden;
  }
  .card--front { left: 37px; }
  .card--back { left: 620px; }

  .front-mark {
    position: absolute;
    inset: 0;
    display: flex;
    align-items: center;
    justify-content: center;
    font-weight: 600;
    font-size: 330px;
    line-height: 1;
    letter-spacing: -10px;
    color: var(--brown);
    padding-top: 10px;
  }

  .back-disc {
    position: absolute;
    left: -158px;
    top: -2px;
    width: 316px;
    height: 316px;
    border-radius: 50%;
    background: var(--brown);
  }
  .back-mark {
    position: absolute;
    left: 0;
    top: 97px;
    width: 125px;
    text-align: center;
    font-weight: 600;
    font-size: 96px;
    line-height: 1;
    letter-spacing: -4px;
    color: var(--paper);
  }

  .contact {
    position: absolute;
    left: 145px;
    top: 95px;
    width: 385px;
    text-align: center;
    color: var(--brown);
  }
  .contact__name {
    font-weight: 600;
    font-size: 41px;
    line-height: 1;
    letter-spacing: 0.5px;
  }
  .contact__line {
    display: flex;
    align-items: center;
    justify-content: center;
    gap: 4px;
    font-family: "Tinos", "Times New Roman", serif;
    font-size: 20px;
    line-height: 1.45;
  }
  .contact__line--email { margin-top: 4px; padding-left: 10px; }
  .contact__line--phone { padding-left: 6px; }
  .contact__icon { width: 19px; height: 15px; fill: var(--brown); }

  .label {
    position: absolute;
    top: 505px;
    width: 420px;
    text-align: center;
    font-family: "Tinos", "Times New Roman", serif;
    font-size: 62px;
    line-height: 1;
    color: var(--label);
  }
  .label--front { left: 70px; }
  .label--back { left: 697px; }
</style>
</head>
<body>
  <div class="band band--top"></div>

  <section class="card card--front" aria-label="Front of business card">
    <div class="front-mark">GH</div>
  </section>

  <section class="card card--back" aria-label="Back of business card">
    <div class="back-disc"></div>
    <div class="back-mark">GH</div>
    <div class="contact">
      <p class="contact__name">Grant Halloway</p>
      <p class="contact__line contact__line--email">
        <svg class="contact__icon" viewBox="0 0 20 14" aria-hidden="true">
          <path d="M0 0h20v14H0z M1.5 1.2 10 8 18.5 1.2" fill="var(--brown)"/>
          <path d="M1 1l9 7 9-7" fill="none" stroke="#fff" stroke-width="1.4"/>
        </svg>
        <span>Grant.halloway@mailbox.net</span>
      </p>
      <p class="contact__line contact__line--phone">
        <svg class="contact__icon" viewBox="0 0 20 16" aria-hidden="true">
          <path d="M1 5c0-3 4-4 9-4s9 1 9 4v1h-5V4H6v2H1z"/>
          <path d="M5 7h10l3 8H2z"/>
          <circle cx="10" cy="11" r="2.2" fill="#fff"/>
        </svg>
        <span>555-014-2298</span>
      </p>
    </div>
  </section>

  <p class="label label--front">front card</p>
  <p class="label label--back">back card</p>

  <div class="band band--bottom"></div>
</body>
</html>
```